Need posters that inspire entrepreneurs

I want to create beautiful, inspiring wall art. I'm looking for a designer to create an awesome sample (note this sample is not for real use). The winning design will form the foundation of our art "style" so there will be LOTS of ongoing work for the winning designer.

It's your challenge to create a style that is clean, inspiring and timeless, and possibly can be adapted to different colour palettes.

Looking for a perfect execution of words, image and design.

The attached example shows one idea. It should serve as an idea only.

Format of the images should be either rectangular or square. Exact size is preferably UK A4 (US letter) or max A3. Assume that a display would consist of a 4 x 4 image grid so size needs to allow for that in a small to medium size office.

The quotes I want in the 3 samples (each in an individual poster - not combined in 1 poster). Each quote should have it's own, the reason for three is to prove the design work on more than one quote. The quotes are:

1) Failure is the condiment that gives success its flavor.
– Dorian Welsby

2) Whether you think you can or think you can’t, you’re right.
– Oswald Pike

3) Ever tried. Ever failed. No matter. Try Again. Fail again. Fail better.
– Lionel Marwick

Each design should include the image of the person and the quote + any design elements you consider relevant. You should find relevant images of the individuals being quoted. The final images will not be published or used commercially in any way.

Font styles to use
Serif
Sans Serif

Colors

Designer to choose colors to be used in the design.

Requirements
Must have
• Words and headshot image - 1 per poster design.
• Please consider in the design that there will not always be photographs of the person quoted and as such the design will need to hold, whether the source is a photo, sketch or something else.
Nice to have
• None, but note that the final image will be printed on a wall mounted board, printed to the edge but not on the edge. The board will have black or white edges so consider in the design.
Should not have
• None

```html
<!DOCTYPE html>
<html lang="en">
<head>
<meta charset="utf-8">
<title>Quote Posters</title>
<link href="https://fonts.googleapis.com/css2?family=Courier+Prime&family=Mrs+Saint+Delafield&display=swap" rel="stylesheet">
<style>
  :root {
    --paper: #ffffff;
    --ink: #ffffff;
    --slate: #3f4a6c;
    --slate-deep: #2c3552;
    --slate-light: #5b6688;
    --orange: #e27d2b;
    --orange-deep: #c9611a;
    --orange-light: #f19a48;
    --plum: #7a3d8e;
    --plum-deep: #5c2a6e;
    --plum-light: #9452a8;
    --photo-dark: #2b2b2b;
    --photo-mid: #8a8a8a;
    --photo-light: #d6d6d6;
    --signature-warm: #fbe6cf;
  }
  html, body {
    margin: 0;
    padding: 0;
    width: 1200px;
    height: 2816px;
    overflow: hidden;
    background: var(--paper);
  }
  .poster-strip {
    position: relative;
    width: 1200px;
    height: 2816px;
  }
  .poster {
    position: absolute;
    left: 0;
    width: 1200px;
    overflow: hidden;
  }
  .poster--ford { top: 0; height: 928px; background: var(--slate); }
  .poster--capote { top: 944px; height: 920px; background: var(--orange); }
  .poster--beckett { top: 1880px; height: 936px; background: var(--plum); }

  .backdrop {
    position: absolute;
    inset: 0;
    opacity: 0.55;
  }
  .poster--ford .backdrop {
    background: linear-gradient(160deg, var(--slate-light) 0%, var(--slate) 45%, var(--slate-deep) 100%);
  }
  .poster--capote .backdrop {
    background: linear-gradient(170deg, var(--orange-light) 0%, var(--orange) 50%, var(--orange-deep) 100%);
  }
  .poster--beckett .backdrop {
    background: radial-gradient(ellipse at 40% 75%, var(--plum-light) 0%, var(--plum) 50%, var(--plum-deep) 100%);
  }

  .portrait {
    position: absolute;
    bottom: 0;
    border-radius: 48% 48% 0 0 / 38% 38% 0 0;
    background: linear-gradient(180deg, var(--photo-light) 0%, var(--photo-mid) 45%, var(--photo-dark) 100%);
  }
  .poster--ford .portrait { left: 580px; width: 540px; height: 720px; }
  .poster--capote .portrait { left: 640px; width: 560px; height: 680px; }
  .poster--beckett .portrait { left: 620px; width: 540px; height: 690px; }

  .quote {
    position: absolute;
    left: 56px;
    margin: 0;
    font-family: "Courier Prime", "Courier New", monospace;
    font-size: 62px;
    line-height: 94px;
    color: var(--ink);
    letter-spacing: 1px;
    z-index: 2;
  }
  .poster--ford .quote { top: 34px; }
  .poster--capote .quote { top: 40px; }
  .poster--beckett .quote { top: 32px; line-height: 96px; }

  .signature {
    position: absolute;
    left: 180px;
    margin: 0;
    font-family: "Mrs Saint Delafield", cursive;
    font-size: 80px;
    line-height: 1;
    color: var(--ink);
    z-index: 2;
  }
  .poster--ford .signature { top: 350px; }
  .poster--capote .signature { top: 390px; color: var(--signature-warm); }
  .poster--beckett .signature { top: 520px; }
</style>
</head>
<body>
<main class="poster-strip">
  <section class="poster poster--ford">
    <div class="backdrop" role="img" aria-label="Faded photo of an early automobile assembly line"></div>
    <div class="portrait" role="img" aria-label="Black and white portrait of Oswald Pike"></div>
    <blockquote class="quote">Whether you think you can or<br>think you can't,<br>you're right.</blockquote>
    <p class="signature">Oswald Pike</p>
  </section>

  <section class="poster poster--capote">
    <div class="backdrop" role="img" aria-label="Faded collage of book covers in orange tones"></div>
    <div class="portrait" role="img" aria-label="Black and white portrait of Dorian Welsby holding a cigarette"></div>
    <blockquote class="quote">Failure is the condiment<br>that gives success<br>its flavor.</blockquote>
    <p class="signature">Dorian Welsby</p>
  </section>

  <section class="poster poster--beckett">
    <div class="backdrop" role="img" aria-label="Faded enlarged portrait in purple tones"></div>
    <div class="portrait" role="img" aria-label="Black and white portrait of Lionel Marwick"></div>
    <blockquote class="quote">Ever tried. Ever failed.<br>No matter.<br>Try Again.<br>Fail again.<br>Fail better.</blockquote>
    <p class="signature">Lionel Marwick</p>
  </section>
</main>
</body>
</html>
```